Velvet Dare Age Verification Landing Page

To create a visually appealing design for the landing page of the adult game "Velvet Dare" that confirms the visitor's age.
The design should have a simple and visually appealing look that focuses on two buttons labeled "Yes" and "No". The purpose of the page is to confirm that the visitor is 18 years of age or older before accessing the game's content. Responsive design that works well on desktop and mobile devices. The final output should be delivered in PSD, AI, or Sketch format, along with any necessary images or assets.
I have also attached examples.

```html
<!DOCTYPE html>
<html lang="en">
<head>
<meta charset="utf-8">
<title>Velvet Dare – Age Verification</title>
<link rel="stylesheet" href="https://fonts.googleapis.com/css2?family=Barlow:wght@500;600&family=Inter:wght@400;500&display=swap">
<style>
  :root {
    --bg-dark: #1a1414;
    --photo-warm: #6b4a3c;
    --photo-deep: #2a1e1c;
    --panel: rgba(132, 62, 148, 0.78);
    --panel-edge: #8d4aa3;
    --accent: #7a2f98;
    --accent-bright: #a45cc2;
    --frame-light: #c79ad6;
    --text: #ffffff;
  }
  * { box-sizing: border-box; margin: 0; padding: 0; }
  html, body { width: 833px; height: 1200px; overflow: hidden; background: var(--bg-dark); }
  .page {
    position: relative;
    width: 833px;
    height: 1200px;
    overflow: hidden;
    font-family: "Inter", sans-serif;
    color: var(--text);
  }
  .hero-photo {
    position: absolute;
    inset: 0;
    background:
      radial-gradient(ellipse 55% 40% at 55% 30%, rgba(170, 120, 95, 0.55), transparent 70%),
      radial-gradient(ellipse 60% 45% at 40% 75%, rgba(150, 100, 90, 0.4), transparent 70%),
      linear-gradient(180deg, var(--photo-warm) 0%, var(--photo-deep) 60%, #3a2e2c 100%);
  }
  .hero-shade { position: absolute; inset: 0; background: rgba(20, 14, 14, 0.35); }

  .brand {
    position: absolute;
    left: 92px;
    top: 88px;
    display: flex;
    align-items: center;
    gap: 12px;
    font-family: "Barlow", sans-serif;
    font-weight: 600;
    font-size: 36px;
    color: var(--text);
  }
  .brand-dot { width: 18px; height: 18px; border-radius: 50%; background: var(--accent-bright); }

  .music-toggle {
    position: absolute;
    left: 663px;
    top: 50px;
    width: 95px;
    height: 95px;
    border-radius: 18px;
    background: var(--accent);
    box-shadow: 0 0 24px rgba(164, 92, 194, 0.6);
    display: flex;
    align-items: center;
    justify-content: center;
    border: none;
  }

  .verify-panel {
    position: absolute;
    left: 77px;
    top: 405px;
    width: 683px;
    height: 642px;
    background: var(--panel);
    text-align: center;
  }
  .panel-frame { position: absolute; left: 0; top: 0; overflow: visible; pointer-events: none; }

  .verify-title {
    font-family: "Barlow", sans-serif;
    font-weight: 500;
    font-size: 62px;
    line-height: 1;
    margin-top: 76px;
  }
  .title-dots {
    display: flex;
    justify-content: center;
    gap: 5px;
    margin-top: 26px;
  }
  .title-dots span { width: 12px; height: 12px; background: var(--text); }
  .verify-text {
    font-size: 28px;
    line-height: 53px;
    margin: 24px auto 0;
    width: 370px;
  }
  .verify-actions {
    position: absolute;
    top: 480px;
    left: 120px;
    display: flex;
    gap: 33px;
  }
  .btn {
    width: 205px;
    height: 80px;
    border-radius: 6px;
    font-family: "Barlow", sans-serif;
    font-weight: 600;
    font-size: 30px;
    color: var(--text);
    display: flex;
    align-items: center;
    justify-content: center;
    gap: 44px;
  }
  .btn-yes { background: var(--accent); border: none; }
  .btn-no { background: transparent; border: 3px solid var(--text); }
</style>
</head>
<body>
<main class="page">
  <div class="hero-photo" role="img" aria-label="Background photograph of a woman with long blonde hair lying on a bed"></div>
  <div class="hero-shade"></div>

  <div class="brand"><span class="brand-dot"></span>Velvet Dare</div>

  <button class="music-toggle" aria-label="Toggle music">
    <svg width="40" height="40" viewBox="0 0 24 24" fill="#fff">
      <path d="M9 3v12.3A3.5 3.5 0 1 0 11 18.5V8h8v5.3A3.5 3.5 0 1 0 21 16.5V3z"/>
    </svg>
  </button>

  <section class="verify-panel">
    <svg class="panel-frame" width="683" height="642" viewBox="0 0 683 642">
      <g fill="var(--panel-edge)">
        <rect x="-6" y="20" width="6" height="300"/>
        <rect x="683" y="360" width="6" height="250"/>
        <rect x="0" y="0" width="40" height="6"/>
        <rect x="400" y="-6" width="240" height="6"/>
        <rect x="80" y="642" width="180" height="6"/>
        <rect x="530" y="642" width="150" height="6"/>
      </g>
      <g fill="var(--frame-light)">
        <rect x="-14" y="110" width="10" height="120"/>
        <rect x="685" y="370" width="10" height="100"/>
        <rect x="120" y="634" width="80" height="6"/>
        <rect x="560" y="634" width="50" height="6"/>
      </g>
      <g fill="#fff" opacity="0.7">
        <rect x="450" y="-6" width="50" height="3"/>
        <rect x="240" y="636" width="200" height="2"/>
        <rect x="676" y="60" width="2" height="140"/>
      </g>
    </svg>

    <h1 class="verify-title">Velvet Dare</h1>
    <div class="title-dots"><span></span><span></span><span></span><span></span><span></span></div>
    <p class="verify-text">Confirm that the visitor is 18 years of age or older before accessing the game's content.</p>

    <div class="verify-actions">
      <button class="btn btn-yes">YES
        <svg width="28" height="28" viewBox="0 0 24 24" fill="none" stroke="#fff" stroke-width="3.5" stroke-linecap="round" stroke-linejoin="round"><path d="M4 12.5l5 5L20 6.5"/></svg>
      </button>
      <button class="btn btn-no">NO
        <svg width="22" height="22" viewBox="0 0 24 24" fill="none" stroke="#fff" stroke-width="4" stroke-linecap="round"><path d="M5 5l14 14M19 5L5 19"/></svg>
      </button>
    </div>
  </section>
</main>
</body>
</html>
```